We Are Corvale Marketing Collateral

We Are Corvale has undergone a rebrand with new logo, website, and intranet design builds. The business is now looking to update its marketing collateral with the new logo design and colour palette. Deliverables include PowerPoint template, Report template, Letterhead, and Email signature. Refer attached design brief for more information. Also attached are the logo and brand document.
Target Market(s)
Executive & Board of SME impact organisations.
Industry/Entity Type
We serve small to medium organisations who are delivering impact, not-for-profits, social enterprises and purpose driven organisations.
Font styles to use
Other font styles liked:
- Roca Two Thin, Rubik Regular
Look and feel
Each slider illustrates characteristics of the customer's brand and the style your logo design should communicate.

```html
<!DOCTYPE html>
<html lang="en">
<head>
<meta charset="utf-8">
<title>We Are Corvale – Letterhead</title>
<link href="https://fonts.googleapis.com/css2?family=Open+Sans:wght@400;600&display=swap" rel="stylesheet">
<style>
  :root {
    --backdrop: #ececec;
    --paper: #fafafa;
    --teal: #1f5a50;
    --text: #5a5a5a;
    --contact: #4a4a4a;
    --ink: #e6e7ea;
  }
  * { margin: 0; padding: 0; box-sizing: border-box; }
  html, body { width: 1200px; height: 803px; overflow: hidden; background: var(--backdrop); }
  body { font-family: "Open Sans", sans-serif; }
  .letterhead {
    position: absolute; left: 327px; top: 21px;
    width: 545px; height: 760px;
    background: var(--paper);
    box-shadow: 0 1px 4px rgba(0,0,0,0.12);
    color: var(--text);
  }
  .brand {
    position: absolute; left: 49px; top: 52px;
    display: flex; align-items: center; gap: 10px;
  }
  .brand-dot { width: 44px; height: 44px; border-radius: 50%; background: var(--teal); }
  .brand-name { font-size: 25px; font-weight: 400; color: var(--teal); letter-spacing: 1px; }
  .contact {
    position: absolute; right: 50px; top: 47px;
    font-size: 10.5px; line-height: 14.5px; color: var(--contact);
    list-style: none;
  }
  .contact li { display: flex; align-items: center; gap: 4px; }
  .contact svg { width: 9px; height: 9px; fill: var(--teal); }
  .letter-body {
    position: absolute; left: 49px; top: 196px; width: 440px;
    font-size: 9.9px; line-height: 14.6px; text-align: justify;
  }
  .letter-body p { margin-bottom: 14.6px; }
  .signature {
    position: absolute; left: 49px; top: 578px;
    width: 62px; height: 60px;
    background: var(--ink);
  }
  .sender {
    position: absolute; left: 49px; top: 688px;
    font-size: 10.8px; line-height: 14px; color: var(--contact);
  }
  .sender .sender-name { color: var(--teal); font-weight: 600; }
</style>
</head>
<body>
  <main class="letterhead">
    <header class="brand">
      <span class="brand-dot"></span>
      <span class="brand-name">CORVALE</span>
    </header>

    <ul class="contact">
      <li><svg viewBox="0 0 10 10"><path d="M2 0.5l2 2-1 1.2c.6 1.3 1.6 2.3 2.9 2.9l1.2-1 2 2-1.3 1.9C4.5 9.3.7 5.5 0.5 1.8z"/></svg>+15550123498</li>
      <li><svg viewBox="0 0 10 10"><path d="M0 1.5h10v7H0zM1 2.5l4 3 4-3v-.1H1z" fill-rule="evenodd"/></svg>hello@corvale.co</li>
      <li><svg viewBox="0 0 10 10"><circle cx="5" cy="5" r="4.2" fill="none" stroke="#1f5a50" stroke-width="1.1"/><path d="M1 5h8M5 .8c-2 2.6-2 5.8 0 8.4M5 .8c2 2.6 2 5.8 0 8.4" fill="none" stroke="#1f5a50" stroke-width=".8"/></svg>www.corvale.co</li>
    </ul>

    <section class="letter-body">
      <p>Dear customer,</p>
      <p>Lorem ipsum dolor sit amet, consectetur adipisicing elit, sed do eiusmod tempor incididunt ut labore et dolore magna aliqua. Ut enim ad minim veniam, quis nostrud exercitation ullamco laboris nisi ut aliquip ex ea commodo consequat. Duis aute irure dolor in reprehenderit in voluptate velit esse cillum dolore eu fugiat nulla pariatur. Excepteur sint occaecat cupidatat non proident, sunt in culpa qui officia deserunt mollit anim id est laborum.</p>
      <p>Lorem ipsum dolor sit amet, consectetur adipisicing elit, sed do eiusmod tempor incididunt ut labore et dolore magna aliqua. Ut enim ad minim veniam, quis nostrud exercitation ullamco laboris nisi ut aliquip ex ea commodo consequat. Duis aute irure dolor in reprehenderit in voluptate velit esse cillum dolore eu fugiat nulla pariatur. Excepteur sint occaecat cupidatat non proident, sunt in culpa qui officia deserunt mollit anim id est laborum.</p>
      <p>Lorem ipsum dolor sit amet, consectetur adipisicing elit, sed do eiusmod tempor incididunt ut labore et dolore magna aliqua. Ut enim ad minim veniam, quis nostrud exercitation ullamco laboris nisi ut aliquip ex ea commodo consequat. Duis aute irure dolor in reprehenderit in voluptate velit esse cillum dolore eu fugiat nulla pariatur. Excepteur sint occaecat cupidatat non proident, sunt in culpa qui officia deserunt mollit anim id est laborum.</p>
      <p>Lorem ipsum dolor sit amet, consectetur adipisicing elit, sed do eiusmod tempor incididunt ut labore et dolore magna aliqua. Ut enim ad minim veniam, quis nostrud exercitation ullamco laboris nisi ut aliquip ex ea commodo consequat. Duis aute irure dolor in reprehenderit.</p>
      <p>Yours Sincerely,</p>
    </section>

    <div class="signature" role="img" aria-label="Handwritten signature of the sender"></div>

    <footer class="sender">
      <div class="sender-name">We Are Corvale</div>
      <div>48 Alder Grove Road,</div>
      <div>Fernbrook, ON K2P 7R4</div>
    </footer>
  </main>
</body>
</html>
```